Poetry Book Cover Design Project

Looking for a minimalistic book cover design for a collection of poems. The book title is "Before The Morning Turns To Glass". There are three parts to the book. First covers poetry in the theme of Rage. Second love and desire. The third is strange poems. Essentially the sections are "Rage", "Desire" and the "Strange". The reason for the title "Before The Morning Turns To Glass" is as if someone is writing these till life changes towards the intended outcome as felt in each poem. I want to have the author's name "Nirosha Kulathunge" at the bottom. Ilustration attached.
- Minimalistic

```html
<!DOCTYPE html>
<html lang="en">
<head>
<meta charset="utf-8">
<title>Before The Morning Turns To Glass — Cover</title>
<link rel="stylesheet" href="https://fonts.googleapis.com/css2?family=Cormorant+Garamond:wght@500;600&display=swap">
<style>
  :root {
    --page: #ffffff;
    --frame: #e9e9e9;
    --rage: #b5463c;
    --desire: #d8718a;
    --strange: #4e8c88;
    --ink: #1d1d1d;
    --title-ink: #ffffff;
  }
  * { box-sizing: border-box; margin: 0; padding: 0; }
  html, body {
    width: 1200px;
    height: 842px;
    overflow: hidden;
    background: var(--page);
  }
  .cover {
    position: absolute;
    left: 324px;
    top: 31px;
    width: 552px;
    height: 780px;
    background: var(--page);
    border: 8px solid var(--frame);
    overflow: hidden;
  }
  .title {
    font-weight: normal;
  }
  .pane {
    position: absolute;
    left: 50%;
    width: 208px;
    height: 108px;
    margin-left: -104px;
    display: flex;
    flex-direction: column;
    align-items: center;
    justify-content: center;
    color: var(--title-ink);
    font-family: "Cormorant Garamond", Georgia, serif;
    font-weight: 600;
    font-size: 24px;
    line-height: 1.15;
    letter-spacing: 3px;
    text-align: center;
  }
  .pane span { display: block; }
  .pane--rage {
    top: 170px;
    transform: translateX(-26px);
    background: var(--rage);
  }
  .pane--desire {
    top: 300px;
    background: var(--desire);
  }
  .pane--strange {
    top: 430px;
    transform: translateX(26px);
    background: var(--strange);
  }
  .rule {
    position: absolute;
    left: 50%;
    top: 600px;
    width: 48px;
    height: 1px;
    margin-left: -24px;
    background: var(--ink);
  }
  .author {
    position: absolute;
    left: 0;
    right: 0;
    top: 692px;
    text-align: center;
    font-family: "Cormorant Garamond", Georgia, serif;
    font-weight: 500;
    font-size: 20px;
    letter-spacing: 7px;
    color: var(--ink);
  }
</style>
</head>
<body>
  <main class="cover">
    <h1 class="title">
      <div class="pane pane--rage"><span>Before</span><span>The</span></div>
      <div class="pane pane--desire"><span>Morning</span><span>Turns</span></div>
      <div class="pane pane--strange"><span>To</span><span>Glass</span></div>
    </h1>
    <div class="rule"></div>
    <p class="author">Nirosha Kulathunge</p>
  </main>
</body>
</html>
```